Business Card Design Project

We are a commercial talent casting company, a very "now" company. We need a new business card that is both current, graphic and elegantly interesting. As we are a service business,
we need something that will attract the attention of new clients,
yet project a business that is 25 years old.

Industry/Entity Type

Business

Requirements
Must have
• 1. Logo - Nora Quillan Casting
2. Address - 47 Harwick Street
New York, New York 10027
3. Phone - 212-638-4170
4. E-Mail - Casting@noraquillan.com

Nice to have
• Would like the card in black and white with the only accent
color being red.

```html
<!DOCTYPE html>
<html lang="en">
<head>
<meta charset="utf-8">
<title>Nora Quillan Casting — Business Card</title>
<link rel="stylesheet" href="https://fonts.googleapis.com/css2?family=Michroma&family=Questrial&display=swap">
<style>
  :root {
    --card-black: #000000;
    --name-grey: #4b5159;
    --accent-red: #e3211f;
    --detail-white: #f2f2f2;
    --stage-light: #f4f4f4;
    --stage-mid: #a9a9a9;
    --stage-dark: #4e4e4e;
    --frame-line: #2a2a2a;
  }
  * { margin: 0; padding: 0; box-sizing: border-box; }
  html, body {
    width: 1200px;
    height: 1194px;
    overflow: hidden;
  }
  .presentation {
    position: relative;
    width: 1200px;
    height: 1194px;
    border: 2px solid var(--frame-line);
    background: radial-gradient(ellipse 900px 1000px at 240px 720px,
      var(--stage-light) 0%, var(--stage-mid) 55%, var(--stage-dark) 100%);
  }
  .card {
    position: absolute;
    width: 834px;
    height: 476px;
    border-radius: 82px;
    background: var(--card-black);
  }
  .card--front { left: 75px; top: 103px; }
  .card--back  { left: 273px; top: 605px; }

  .line {
    position: absolute;
    left: 0;
    width: 100%;
    text-align: center;
    transform: translateY(-50%);
    white-space: nowrap;
    line-height: 1;
  }
  .brand-name {
    font-family: "Michroma", "Arial", sans-serif;
    color: var(--name-grey);
    letter-spacing: 5px;
  }
  .brand-role {
    font-family: "Michroma", "Arial", sans-serif;
    color: var(--accent-red);
    letter-spacing: 5px;
  }
  .card--front .brand-name,
  .card--front .brand-role { font-size: 34px; }
  .card--front .first  { top: 180px; }
  .card--front .last   { top: 237px; }
  .card--front .brand-role { top: 296px; }

  .card--back .brand-name { top: 135px; font-size: 33px; letter-spacing: 6px; }
  .card--back .brand-role { top: 196px; font-size: 34px; letter-spacing: 6px; }

  .contact {
    font-family: "Questrial", "Arial", sans-serif;
    font-variant: small-caps;
    font-size: 25px;
    letter-spacing: 3px;
    color: var(--detail-white);
  }
  .contact.street { top: 250px; }
  .contact.city   { top: 281px; }
  .contact.phone  { top: 313px; }
  .contact.email  { top: 345px; }
</style>
</head>
<body>
  <main class="presentation">
    <section class="card card--front" aria-label="Card front">
      <p class="line brand-name first">NORA</p>
      <p class="line brand-name last">QUILLAN</p>
      <p class="line brand-role">CASTING</p>
    </section>

    <section class="card card--back" aria-label="Card back">
      <p class="line brand-name">NORA QUILLAN</p>
      <p class="line brand-role">CASTING</p>
      <p class="line contact street">47 Harwick Street</p>
      <p class="line contact city">New York,&nbsp; 10027</p>
      <p class="line contact phone">212-638-4170</p>
      <p class="line contact email">Casting@noraquillan.com</p>
    </section>
  </main>
</body>
</html>
```